Law Firm Business Card

This is a business card for a law firm that serves US military and veterans.

The card must have ONLY the following (we want an uncluttered look):

- Company logo (PNG, GIF, JPEG copies uploaded)
- A tagline reading: "a law firm for service members and veterans"
- My name and title: "Martin Okello" and "Attorney"
- My email: "martin.okello@harborlinecounsel.com"
- My number: "855-FILE-NOW (345-3669)"

We are looking for a clean, simple layout with only the above information, likely printed on a bright white cotton stock. The font of our logo is DIN 1451, and the font used on our website is Helvetica Neue. The color of our logo is #336699, and we probably want the tagline in that color also, and my contact information in a dark grey. Please review our website at www.harborlinecounsel.com to ensure your card design complements our website style.

Thanks and we look forward to seeing your submissions.

A few notes:

- Two-sided submissions are ok
- Please don't add graphics (scales of justice, judges hammer, etc)

```html
<!DOCTYPE html>
<html lang="en">
<head>
<meta charset="utf-8">
<title>Harborline Counsel – Business Card</title>
<link href="https://fonts.googleapis.com/css2?family=Roboto+Condensed:wght@400;700&display=swap" rel="stylesheet">
<style>
  :root {
    --brand-blue: #336699;
    --band-blue: #34689a;
    --ink-grey: #3c3c3c;
    --rule-grey: #555555;
    --paper: #ffffff;
  }
  html, body {
    margin: 0;
    padding: 0;
    width: 1200px;
    height: 720px;
    overflow: hidden;
    background: var(--paper);
  }
  .card {
    position: relative;
    width: 1200px;
    height: 720px;
    background: var(--paper);
    font-family: "Roboto Condensed", "Helvetica Neue", Arial, sans-serif;
  }
  .wordmark {
    position: absolute;
    top: 62px;
    left: 0;
    width: 1200px;
    text-align: center;
    color: var(--brand-blue);
    font-weight: 700;
    text-transform: uppercase;
    line-height: 1;
  }
  .wordmark-primary {
    display: block;
    font-size: 88px;
    letter-spacing: 1px;
  }
  .wordmark-secondary {
    display: block;
    margin-top: 6px;
    font-size: 44px;
    letter-spacing: 6px;
  }
  .identity-band {
    position: absolute;
    top: 297px;
    left: 0;
    width: 1200px;
    height: 195px;
    background: var(--band-blue);
    color: var(--paper);
    text-align: center;
  }
  .person-name {
    margin: 44px 0 0;
    font-size: 50px;
    font-weight: 700;
    text-transform: uppercase;
    letter-spacing: 0.5px;
    line-height: 1;
  }
  .tagline {
    margin: 22px 0 0;
    font-size: 28px;
    font-weight: 400;
    line-height: 1;
  }
  .contact-row {
    position: absolute;
    top: 650px;
    left: 0;
    width: 1200px;
    height: 46px;
    color: var(--ink-grey);
    font-size: 32px;
    line-height: 46px;
  }
  .contact-item {
    position: absolute;
    top: 0;
    display: flex;
    align-items: center;
    gap: 10px;
    white-space: nowrap;
  }
  .contact-phone { left: 82px; }
  .contact-email { left: 556px; }
  .contact-divider {
    position: absolute;
    left: 513px;
    top: -8px;
    width: 1px;
    height: 56px;
    background: var(--rule-grey);
  }
  .contact-icon { flex: none; }
</style>
</head>
<body>
  <div class="card">
    <div class="wordmark" aria-label="Harborline Counsel">
      <span class="wordmark-primary">Harborline</span>
      <span class="wordmark-secondary">Counsel</span>
    </div>

    <section class="identity-band">
      <h1 class="person-name">Martin Okello and Attorney</h1>
      <p class="tagline">a law firm for service members and veteran</p>
    </section>

    <div class="contact-row">
      <div class="contact-item contact-phone">
        <svg class="contact-icon" width="20" height="34" viewBox="0 0 20 34" aria-hidden="true">
          <rect x="1" y="1" width="18" height="32" rx="3" fill="var(--ink-grey)"/>
          <rect x="4" y="5" width="12" height="9" fill="var(--paper)"/>
          <g fill="var(--paper)">
            <rect x="4" y="17" width="3" height="3"/><rect x="8.5" y="17" width="3" height="3"/><rect x="13" y="17" width="3" height="3"/>
            <rect x="4" y="22" width="3" height="3"/><rect x="8.5" y="22" width="3" height="3"/><rect x="13" y="22" width="3" height="3"/>
            <rect x="4" y="27" width="3" height="3"/><rect x="8.5" y="27" width="3" height="3"/><rect x="13" y="27" width="3" height="3"/>
          </g>
        </svg>
        <span>855-FILE-NOW (345-3669)</span>
      </div>
      <div class="contact-divider"></div>
      <div class="contact-item contact-email">
        <svg class="contact-icon" width="30" height="22" viewBox="0 0 30 22" aria-hidden="true">
          <rect x="1.5" y="1.5" width="27" height="19" fill="none" stroke="var(--ink-grey)" stroke-width="2.5"/>
          <path d="M1.5 1.5 L15 12 L28.5 1.5 M1.5 20.5 L11.5 10 M28.5 20.5 L18.5 10" fill="none" stroke="var(--ink-grey)" stroke-width="2.5"/>
        </svg>
        <span>martin.okello@harborlinecounsel.com</span>
      </div>
    </div>
  </div>
</body>
</html>
```